Präsentationsvorlagen für Hausarztpraxis
Zielgruppe
Neue Hausarztpraxis, Zielgruppe junge Patienten
Es ist gedacht für eine Präsentation die im WArtezimmer auf dem T V läuft... daher seitenaufbau variieren.
Aufgabenstellung
es sollte zum Logo passen.. modern sein, verschiedene Seiten ( nicht jede Seite sollte gleich aussehen) ich sollte es mit Pages bearbeiten können. In der Präsentation soll die Praxis vorgstellt werden, mit den Sprechzeiten, Website, dem Team, Dem leistungsspektrum, erweiterte Dinge wie NEU Ultraschalluntersuchungen der Schilddrüse, Bauch und Gefäße, auch eine Seite zu den neuen Hyaloronsäure Fillern... ich werden heute Abend noch mehr schreiben was mit untergebracht werden sollte
Farbe bitte wie das Logo halten...

```html
<!DOCTYPE html>
<html lang="de">
<head>
<meta charset="utf-8">
<title>Präsentationsvorlagen Hausarztpraxis</title>
<link href="https://fonts.googleapis.com/css2?family=Fira+Sans:wght@400;700&display=swap" rel="stylesheet">
<style>
:root{
  --crimson:#c8234a;
  --coral:#f0405c;
  --board:#e9e6e3;
  --paper:#ffffff;
  --ink:#4a4a4a;
  --num:#333;
}
*{margin:0;padding:0;box-sizing:border-box}
html,body{width:1200px;height:768px;overflow:hidden;background:var(--board);font-family:"Fira Sans",sans-serif}
.board{position:relative;width:1200px;height:768px}
.slide{position:absolute;width:374px;height:210px;background:var(--paper);border-radius:4px;overflow:hidden;box-shadow:0 0 0 1px #d8d4d0}
.num{position:absolute;font-size:11px;color:var(--num)}
.abs{position:absolute}
.crimson{background:var(--crimson)}
.coral{background:var(--coral)}
.photo{position:absolute}
h2{position:absolute;color:var(--crimson);font-weight:700;line-height:1.12}
.body{position:absolute;color:var(--ink);font-size:6.6px;line-height:1.45}
.body p+p{margin-top:6px}
.accent{color:var(--crimson)}
.brand{position:absolute;display:flex;align-items:center;gap:3px;color:var(--crimson);font-size:5.5px;font-weight:700;white-space:nowrap}
.brand .dot{width:9px;height:9px;border-radius:50%;background:var(--crimson)}
.white{color:#fff}
.white .dot{background:#fff}
ul.steps{list-style:none;margin-top:4px}
ul.steps li{padding-left:10px;position:relative}
ul.steps li::before{content:"–";position:absolute;left:0}
.member{position:absolute;top:77px;width:75px}
.member .photo{position:relative;width:75px;height:93px;background:linear-gradient(180deg,#d9d9dc 0%,#d6d3d6 55%,#e0307a 56%,#e0307a 100%)}
.member .tag{position:absolute;top:91px;left:-11px;width:76px;height:27px;background:var(--coral);color:#fff;padding:3px 4px;font-size:5.6px;font-weight:700;line-height:1.2}
.member .tag small{display:block;font-weight:400;font-size:4.4px}
.services{position:absolute;left:0;top:105px;width:204px;height:88px;background:var(--crimson);color:#fff;font-size:6.7px;line-height:1.4;padding:11px 10px 0 22px}
</style>
</head>
<body>
<main class="board">

<!-- 1 Welcome -->
<section class="slide" style="left:8px;top:20px">
  <div class="photo" role="img" aria-label="Foto historischer Fachwerkhäuser an einem Marktplatz unter blauem Himmel" style="left:186px;top:0;width:170px;height:210px;background:linear-gradient(180deg,#b9dbe9 0%,#e2eef2 40%,#8d7e78 62%,#6f6a68 100%)"></div>
  <div class="abs crimson" style="left:13px;top:0;width:173px;height:210px"></div>
  <div class="abs coral" style="left:168px;top:6px;width:37px;height:14px"></div>
  <div class="abs coral" style="left:259px;top:146px;width:115px;height:37px"></div>
  <div class="brand" style="left:224px;top:36px;font-size:6.5px"><span class="dot"></span>Dr. med. Johanna Wellbrock</div>
  <h2 class="white" style="left:41px;top:138px;font-size:20px;color:#fff">Herzlich<br>Willkommen!</h2>
</section>
<span class="num" style="left:8px;top:240px">1</span>

<!-- 2 Letter -->
<section class="slide" style="left:413px;top:20px">
  <div class="abs coral" style="left:0;top:142px;width:14px;height:68px"></div>
  <h2 style="left:35px;top:33px;font-size:14.5px">Liebe Patientinnen<br>und Patienten,</h2>
  <div class="body" style="left:35px;top:80px;width:200px">
    <p>Seit 1. Oktober 2021 habe ich nun die Praxis von<br>Herrn Dr. Harder übernommen.</p>
    <p><span class="accent">Mein Werdegang:</span><br>Ärztin in Weiterbildung zum Facharzt für Allgemeinmedizin</p>
    <ul class="steps">
      <li>Medizinstudium in den Jahren 2009 — 2015 an der Universität Tübingen sowie Studium der Zahnmedizin an der Universität Göttingen von 2005 — 2009.</li>
      <li>Berufsbegleitendes Ergänzungsstudium der Ernährungsmedizin im Jahr 2017.</li>
      <li>Promotion am 09.10.2019 in Tübingen</li>
    </ul>
  </div>
  <div class="photo" role="img" aria-label="Porträtfoto der Ärztin im pinken Poloshirt" style="left:240px;top:18px;width:109px;height:173px;background:linear-gradient(180deg,#dcdcde 0%,#d8d6d8 48%,#e0307a 50%,#d92a72 100%)"></div>
  <div class="abs crimson" style="left:356px;top:18px;width:18px;height:173px"></div>
  <div class="body" style="left:252px;top:193px;font-size:6.5px">Dr. med. Johanna Wellbrock</div>
</section>
<span class="num" style="left:413px;top:240px">2</span>

<!-- 3 Hours -->
<section class="slide" style="left:818px;top:20px">
  <div class="photo" role="img" aria-label="Foto eines schwarzen Telefonhörers mit Kabel auf grauem Grund" style="left:33px;top:0;width:155px;height:210px;background:linear-gradient(180deg,#d9d8d4,#cfcdc9)"></div>
  <div class="abs crimson" style="left:13px;top:0;width:2px;height:193px"></div>
  <div class="abs crimson" style="left:13px;top:191px;width:152px;height:2px"></div>
  <div class="abs crimson" style="left:165px;top:0;width:2px;height:193px"></div>
  <div class="abs coral" style="left:127px;top:183px;width:81px;height:14px"></div>
  <div class="brand" style="left:310px;top:20px"><span class="dot"></span>Dr. J. Wellbrock</div>
  <h2 style="left:209px;top:42px;font-size:14.5px">Unsere neuen<br>Sprechstunden</h2>
  <div class="body" style="left:208px;top:89px;width:160px">
    <p>Mo 8-11:30 sowie 14-17 Uhr<br>Die 8-13 Uhr / Mi 8-13 Uhr<br>Do 8-11:30 sowie 14-18 Uhr<br>Fr 8-11:30</p>
    <p>Telefonisch erreichen Sie uns täglich von 8:30-11:00 Uhr sowie Montags und Donnerstags von 14:00-16:00 Uhr.</p>
  </div>
</section>
<span class="num" style="left:818px;top:240px">3</span>

<!-- 4 Website -->
<section class="slide" style="left:8px;top:270px">
  <div class="photo" role="img" aria-label="Foto eines Schreibtischs mit Kaffeetasse, Kirschen, Tastatur und Stift" style="left:5px;top:5px;width:364px;height:200px;background:linear-gradient(135deg,#f4f4f4 0%,#ebebeb 60%,#dedede 100%)"></div>
  <div class="abs crimson" style="left:0;top:48px;width:180px;height:101px"></div>
  <div class="abs coral" style="left:5px;top:40px;width:87px;height:15px"></div>
  <div class="body" style="left:27px;top:71px;width:150px;color:#fff;font-size:6.8px">
    <p>Wir haben eine neue Website, auf der Sie uns gerne besuchen können.</p>
    <p style="font-weight:700;margin-top:9px">www.hausarzt-lindenau.de</p>
    <p style="margin-top:9px">Gerne können Sie auch ab sofort online Ihren Termin vereinbaren.</p>
  </div>
</section>
<span class="num" style="left:8px;top:490px">4</span>

<!-- 5 Team -->
<section class="slide" style="left:413px;top:270px">
  <div class="brand" style="left:303px;top:20px"><span class="dot"></span>Dr. J. Wellbrock</div>
  <h2 style="left:24px;top:40px;font-size:14.5px">Das sind wir – unser Team</h2>
  <div class="member" style="left:25px"><div class="photo" role="img" aria-label="Porträtfoto einer Ärztin im pinken Poloshirt"></div><div class="tag">Dr. med. Johanna Wellbrock<small>Ärztin in Weiterbildung zum Facharzt für Allgemeinmedizin</small></div></div>
  <div class="member" style="left:108px"><div class="photo" role="img" aria-label="Porträtfoto einer Mitarbeiterin im pinken Poloshirt"></div><div class="tag" style="left:-4px">Marion Feldtkamp<small>Kinderkrankenschwester</small></div></div>
  <div class="member" style="left:191px"><div class="photo" role="img" aria-label="Porträtfoto einer Mitarbeiterin im pinken Poloshirt"></div><div class="tag" style="left:-4px">Sabine Rosskopf<small>Medizinische Fachangestellte</small></div></div>
  <div class="member" style="left:275px"><div class="photo" role="img" aria-label="Porträtfoto einer Mitarbeiterin im pinken Poloshirt"></div><div class="tag" style="left:-4px">Petra Lindemann<small>Medizinische Fachangestellte</small></div></div>
</section>
<span class="num" style="left:413px;top:490px">5</span>

<!-- 6 Prescriptions -->
<section class="slide" style="left:818px;top:270px">
  <div class="photo" role="img" aria-label="Foto einer Hand mit Handschuh, die Tablettenblister hält" style="left:150px;top:15px;width:224px;height:179px;background:linear-gradient(90deg,#8a6f62 0%,#d9d6d2 40%,#eeeae6 70%,#7fc3bd 100%)"></div>
  <div class="abs coral" style="left:133px;top:30px;width:241px;height:1.5px"></div>
  <div class="abs coral" style="left:133px;top:30px;width:1.5px;height:179px"></div>
  <div class="abs coral" style="left:133px;top:207px;width:241px;height:1.5px"></div>
  <h2 style="left:22px;top:28px;font-size:14.5px">Rezepte<br>bestellen</h2>
  <div class="body" style="left:22px;top:73px;width:100px">
    <p>Rezepte sollten ein Tag vor Abholung auf unsere Rezepthotline gesprochen werden, oder in den neuen Briefkasten im Hausflur eingeworfen werden.</p>
    <p style="margin-top:8px">Diese werden dann nach der Sprechzeit für sie fertiggestellt</p>
  </div>
</section>
<span class="num" style="left:818px;top:490px">6</span>

<!-- 7 New service -->
<section class="slide" style="left:8px;top:520px">
  <div class="photo" role="img" aria-label="Foto einer Ultraschalluntersuchung mit Gerät und Patientin" style="left:0;top:0;width:140px;height:210px;background:linear-gradient(160deg,#3d4246 0%,#9aa3a8 35%,#e3e6e8 70%,#f3f3f3 100%)"></div>
  <div class="abs crimson" style="left:126px;top:37px;width:29px;height:173px"></div>
  <div class="abs coral" style="left:148px;top:62px;width:14px;height:68px"></div>
  <div class="brand" style="left:302px;top:20px"><span class="dot"></span>Dr. J. Wellbrock</div>
  <h2 style="left:191px;top:60px;font-size:14.5px">NEU im<br>Leistungsspektrum</h2>
  <div class="body" style="left:191px;top:110px;width:155px">
    <p>Ultraschall... da Bauch, Gefäße und Schilddrüse mit Foto vom Gerät SonoView</p>
    <p style="margin-top:8px">Dies ist nicht Umfang des „Check Ups“, kann aber gern als individuelle Gesundheitsleistung (IGeL) in Anspruch genommen werden.</p>
  </div>
</section>
<span class="num" style="left:8px;top:740px">7</span>

<!-- 8 Services -->
<section class="slide" style="left:413px;top:520px">
  <div class="photo" role="img" aria-label="Foto eines hellen Behandlungsraums mit Liege und Hocker" style="left:60px;top:10px;width:314px;height:190px;background:linear-gradient(180deg,#e6e5e3 0%,#dcdbd8 75%,#c9b79c 76%,#bfa987 100%)"></div>
  <div class="brand" style="left:303px;top:20px"><span class="dot"></span>Dr. J. Wellbrock</div>
  <h2 style="left:22px;top:87px;font-size:14.5px">Unser Leistungsspektrum</h2>
  <div class="services">Vollständige hausärztliche Versorgung / Gesundheitsvorsorge / Krebsvorsorge / EKG und Ergometrie / Sonographie Bauch, Schilddrüse, Gefäße / Langzeitblutdruckmessung / Lungenfunktionsprüfung / Laboruntersuchungen / Sämtliche Impfungen / Kleine operative Eingriffe &nbsp;/ Wundversorgung / Autogenes Training / Neuraltherapie</div>
</section>
<span class="num" style="left:413px;top:740px">8</span>

<!-- 9 Contract -->
<section class="slide" style="left:818px;top:520px">
  <div class="abs crimson" style="left:22px;top:0;width:352px;height:18px"></div>
  <div class="abs coral" style="left:236px;top:10px;width:111px;height:15px"></div>
  <div class="brand" style="left:300px;top:47px"><span class="dot"></span>Dr. J. Wellbrock</div>
  <h2 style="left:24px;top:62px;font-size:14.5px">Hausarztvertrag</h2>
  <div class="body" style="left:24px;top:91px;width:280px">
    <p>Im Hausarztprogramm, auch Hausarztzentrierte Versorgung genannt, übernimmt der Hausarzt als Spezialist für den ganzen Menschen die umfassende medizinische Versorgung seiner Patienten.</p>
    <p style="margin-top:8px">Er ist speziell dafür weitergebildet, als erster Ansprechpartner Beschwerden aus ganz unterschiedlichen Bereichen zu behandeln, abzuwägen und bei Bedarf die Koordination mit weiteren Fachärzten, Krankenhäusern und anderen Heilberufen vorzunehmen. Im Anschluss laufen bei ihm alle wichtigen Befunde und Berichte zusammen.</p>
  </div>
</section>
<span class="num" style="left:818px;top:740px">9</span>

</main>
</body>
</html>
```